What makes us Different Managed Communications Services Provider Flyer

We need a flyer to explain why we are different than other "managed IT services" company. Gives a brief description of our company and services that can entice clients and potential clients to setup a FREE consultation with us. This will become part of an ongoing marketing campaign that includes emails, leave behinds, brochures, and more

```html
<!DOCTYPE html>
<html lang="en">
<head>
<meta charset="utf-8">
<title>Harborline Networks – What Makes Us Different</title>
<link href="https://fonts.googleapis.com/css2?family=Bebas+Neue&family=Oswald:wght@300&family=Montserrat:wght@400;600;700&display=swap" rel="stylesheet">
<style>
  :root{
    --navy:#0b47a3;
    --royal:#1560bd;
    --cyan:#38bcd6;
    --accent:#2aaed6;
    --ink:#4a4a4a;
    --dark:#2e2e2e;
    --panel:#ececec;
    --stage:#525252;
    --white:#ffffff;
  }
  *{box-sizing:border-box;margin:0;padding:0}
  html,body{width:1200px;height:1117px;overflow:hidden;background:var(--stage)}
  body{position:relative;font-family:"Montserrat",Arial,sans-serif;color:var(--ink)}
  .page{position:absolute;top:214px;width:532px;height:688px;background:var(--white);overflow:hidden}
  .page--front{left:59px}
  .page--back{left:608px}
  .page > svg{position:absolute;left:0;top:0}
  .abs{position:absolute}
  .body-copy{font-size:9.4px;line-height:12.7px;color:var(--ink)}
  .body-copy p+p{margin-top:12.7px}
  .hl{color:var(--accent);font-weight:700}
  .section-title{position:absolute;display:flex;align-items:center;gap:9px;font-family:"Bebas Neue",sans-serif;font-weight:400;color:var(--navy);font-size:22px;line-height:21px}
  .section-mark{width:11px;height:11px;flex:none;background:linear-gradient(135deg,var(--navy),var(--cyan))}
  .brand{position:absolute;left:42px;top:58px;display:flex;align-items:center;gap:8px}
  .brand-dot{width:18px;height:18px;border-radius:50%;background:var(--royal)}
  .brand-name{font-family:"Montserrat",sans-serif;font-weight:700;font-size:17px;color:var(--dark)}
  .hero-title{position:absolute;left:38px;top:146px;color:var(--white);font-weight:400}
  .hero-title .lead{font-family:"Bebas Neue",sans-serif;font-size:32px;line-height:29px;display:block}
  .hero-title .sub{font-family:"Oswald",sans-serif;font-weight:300;font-size:23px;line-height:28px;display:block;margin-top:2px}
  .site-tab{position:absolute;left:145px;top:646px;width:242px;height:42px;border-radius:14px 14px 0 0;background:linear-gradient(90deg,var(--navy),var(--cyan));display:flex;align-items:center;justify-content:center;gap:8px;color:var(--white);font-weight:700;font-size:13px}
  .site-tab svg{flex:none}
  .service-grid{position:absolute;left:30px;top:164px;width:472px;height:134px;background:var(--panel);border-bottom:4px solid var(--cyan);border-radius:4px}
  .service{position:absolute;display:flex;gap:10px;align-items:flex-start;font-size:9.4px;line-height:12.6px;font-weight:600;color:var(--dark)}
  .service svg{flex:none}
  .closing{position:absolute;left:0;top:607px;width:532px;height:81px;border-top:5px solid var(--navy);background:linear-gradient(90deg,var(--navy),var(--cyan));padding:12px 40px 0 44px;color:var(--white);font-weight:700;font-size:9.4px;line-height:13.3px}
  .rule{position:absolute;left:45px;top:481px;width:437px;height:1px;background:var(--cyan)}
</style>
</head>
<body>

<section class="page page--front">
  <svg width="532" height="688" viewBox="0 0 532 688" aria-hidden="true">
    <defs>
      <linearGradient id="bandGrad" x1="0" x2="1" y1="0" y2="0">
        <stop offset="0" stop-color="#3bbbd6"/><stop offset="1" stop-color="#0b47a3"/>
      </linearGradient>
      <linearGradient id="tabGrad" x1="0" x2="1"><stop offset="0" stop-color="#1f86c9"/><stop offset="1" stop-color="#38bcd6"/></linearGradient>
      <linearGradient id="dropGrad" x1="0" x2="1" y1="0" y2="1"><stop offset="0" stop-color="#38bcd6"/><stop offset="1" stop-color="#1a7fc4"/></linearGradient>
    </defs>
    <rect x="0" y="0" width="532" height="9" fill="#0b47a3"/>
    <path d="M395,9 Q410,9 418,20 Q426,31 440,31 L532,31 L532,9 Z" fill="url(#tabGrad)"/>
    <path d="M0,135 L265,135 Q285,135 295,155 L338,238 L0,238 Z" fill="url(#bandGrad)"/>
    <rect x="0" y="238" width="300" height="8" fill="#e4e4e4"/>
    <circle cx="263" cy="285" r="3.5" fill="#0b47a3"/>
    <polyline points="263,285 358,285 318,212" fill="none" stroke="#0b47a3" stroke-width="1.6"/>
    <path d="M272,335 L272,304 L292,300" fill="none" stroke="#2e3a48" stroke-width="3"/>
    <rect x="327" y="485" width="205" height="6" fill="#0b47a3"/>
    <path d="M309,410 Q292,440 284,460 Q276,490 305,492 L345,492 Q320,470 309,410 Z" fill="url(#dropGrad)"/>
    <rect x="0" y="498" width="532" height="190" fill="#ececec"/>
  </svg>

  <svg width="532" height="300" viewBox="0 0 532 300" role="img" aria-label="Photo of a support agent wearing a headset">
    <defs><linearGradient id="photoA" x1="0" x2="1" y1="0" y2="1"><stop offset="0" stop-color="#c9d6e0"/><stop offset="0.6" stop-color="#6f7f8c"/><stop offset="1" stop-color="#1f2a33"/></linearGradient></defs>
    <path d="M209,17 L385,17 Q397,17 404,28 Q411,38 425,38 L532,38 L532,286 L375,286 Q362,286 357,276 Z" fill="url(#photoA)"/>
  </svg>

  <svg width="532" height="500" viewBox="0 0 532 500" role="img" aria-label="Photo of a smiling support agent with headset at a computer in a bright office">
    <defs><linearGradient id="photoB" x1="0" x2="1" y1="0" y2="1"><stop offset="0" stop-color="#e3e7ea"/><stop offset="0.5" stop-color="#8fb3cf"/><stop offset="1" stop-color="#4b5f72"/></linearGradient></defs>
    <path d="M292,300 L532,300 L532,484 L345,484 Q318,484 312,450 L300,400 Z" fill="url(#photoB)"/>
  </svg>

  <div class="brand"><span class="brand-dot"></span><span class="brand-name">Harborline Networks</span></div>

  <h1 class="hero-title">
    <span class="lead">More than just<br>a managed IT provider</span>
    <span class="sub">OUR LEGACY OF EXCELLENCE</span>
  </h1>

  <div class="abs body-copy" style="left:41px;top:262px;width:222px">
    <p>At our company, we are far more than your typical managed IT provider. Since our founding in 1983, we have built a reputation based on trust, reliability, and unparalleled service. With <span class="hl">client relationships spanning 20 to 30 years,</span> we have demonstrated a level of commitment that few IT firms can match.</p>
    <p>What sets us apart is not just our technical expertise but the <span class="hl">deep, long-term partnerships</span> we cultivate with our clients—many of whom have stayed with us <span class="hl">without ever being locked into a contract.</span> That is a testament to the exceptional quality of our service and the trust we have earned over decades.</p>
  </div>

  <h2 class="section-title" style="left:41px;top:522px"><span class="section-mark"></span>A Commitment Beyond Contracts</h2>
  <div class="abs body-copy" style="left:41px;top:555px;width:450px;line-height:13.4px">
    <p>Unlike many managed IT providers who rely on rigid contracts to retain clients, we believe that service excellence speaks for itself. The longevity of our client relationships is rooted in our ability to <span class="hl">anticipate needs, resolve challenges before they escalate, and proactively enhance network &amp; communication infrastructures.</span> Our <span class="hl">comprehensive checklists, questionnaires, policies, and procedures, attention to details ensure that every client receives a tailored, best-in-class experience from day one.</span></p>
  </div>

  <div class="site-tab">
    <svg width="13" height="13" viewBox="0 0 14 14" aria-hidden="true"><g fill="none" stroke="#7fd8ea" stroke-width="1.2"><circle cx="7" cy="7" r="6"/><ellipse cx="7" cy="7" rx="2.6" ry="6"/><line x1="1" y1="7" x2="13" y2="7"/></g></svg>
    <span>www.harborlinenetworks.com</span>
  </div>
</section>

<section class="page page--back">
  <svg width="532" height="688" viewBox="0 0 532 688" aria-hidden="true">
    <defs><linearGradient id="tabGrad2" x1="0" x2="1"><stop offset="0" stop-color="#1f86c9"/><stop offset="1" stop-color="#38bcd6"/></linearGradient></defs>
    <rect x="0" y="0" width="532" height="9" fill="#0b47a3"/>
    <path d="M395,9 Q410,9 418,20 Q426,31 440,31 L532,31 L532,9 Z" fill="url(#tabGrad2)"/>
    <ellipse cx="266" cy="306" rx="230" ry="6" fill="#dcdcdc"/>
  </svg>

  <svg width="532" height="260" viewBox="0 0 532 260" role="img" aria-label="Photo of a smiling support agent with glasses and headset at a computer">
    <defs><linearGradient id="photoC" x1="0" x2="1" y1="0" y2="1"><stop offset="0" stop-color="#dfe4e6"/><stop offset="0.55" stop-color="#9fbcd6"/><stop offset="1" stop-color="#3f79b6"/></linearGradient></defs>
    <path d="M243,17 L385,17 Q397,17 404,28 Q411,38 425,38 L532,38 L532,239 L380,239 Z" fill="url(#photoC)"/>
  </svg>

  <h2 class="section-title" style="left:45px;top:46px;align-items:flex-start"><span class="section-mark" style="margin-top:5px"></span><span>A Holistic Approach<br>to IT Management</span></h2>
  <div class="abs body-copy" style="left:45px;top:98px;width:255px;line-height:13.3px">
    <p>We don’t just manage IT—we integrate ourselves into your business, ensuring that technology aligns with your strategic goals. Our services go beyond traditional break-fix support; we offer:</p>
  </div>

  <div class="service-grid">
    <div class="service" style="left:16px;top:16px;width:200px">
      <svg width="34" height="36" viewBox="0 0 34 36" aria-hidden="true"><polygon points="17,1 32,9.5 32,26.5 17,35 2,26.5 2,9.5" fill="#1560bd" stroke="#bfe6f2" stroke-width="1.5"/><polyline points="10,23 15,17 19,20 25,13" fill="none" stroke="#fff" stroke-width="1.6"/><line x1="9" y1="25" x2="25" y2="25" stroke="#fff" stroke-width="1.2"/></svg>
      <span>Strategic IT Roadmaps customized to drive business growth.</span>
    </div>
    <div class="service" style="left:236px;top:16px;width:225px">
      <svg width="34" height="36" viewBox="0 0 34 36" aria-hidden="true"><polygon points="17,1 32,9.5 32,26.5 17,35 2,26.5 2,9.5" fill="#1560bd" stroke="#bfe6f2" stroke-width="1.5"/><path d="M11,18 A6,6 0 1 1 17,24" fill="none" stroke="#fff" stroke-width="1.6"/><polyline points="9,16 11,19 14,17" fill="none" stroke="#fff" stroke-width="1.4"/></svg>
      <span>Comprehensive backup and disaster recovery solutions that provide peace of mind.</span>
    </div>
    <div class="service" style="left:16px;top:70px;width:200px">
      <svg width="34" height="36" viewBox="0 0 34 36" aria-hidden="true"><polygon points="17,1 32,9.5 32,26.5 17,35 2,26.5 2,9.5" fill="#1560bd" stroke="#bfe6f2" stroke-width="1.5"/><path d="M17,9 L24,12 L24,18 Q24,24 17,27 Q10,24 10,18 L10,12 Z" fill="none" stroke="#fff" stroke-width="1.4"/><polyline points="13.5,18 16,20.5 20.5,15.5" fill="none" stroke="#fff" stroke-width="1.5"/></svg>
      <span>Proactive cybersecurity assessments that help keep businesses secure.</span>
    </div>
    <div class="service" style="left:236px;top:70px;width:225px">
      <svg width="34" height="36" viewBox="0 0 34 36" aria-hidden="true"><polygon points="17,1 32,9.5 32,26.5 17,35 2,26.5 2,9.5" fill="#1560bd" stroke="#bfe6f2" stroke-width="1.5"/><path d="M10,13 Q9,16 12,21 Q16,26 20,26 L22,23 L19,21 L17,22 Q14,20 13,17 L14,15 L12,12 Z" fill="none" stroke="#fff" stroke-width="1.3"/><circle cx="22" cy="13" r="3.5" fill="none" stroke="#fff" stroke-width="1.2"/></svg>
      <span>Industry-leading response times and dedicated support teams focused on delivering an exceptional client experience.</span>
    </div>
  </div>

  <h2 class="section-title" style="left:45px;top:318px"><span class="section-mark"></span>Our Clients Stay Because We Deliver</h2>
  <div class="abs body-copy" style="left:45px;top:348px;width:440px;line-height:13.4px">
    <p>For over 40 years, we have maintained a standard of excellence that <span class="hl">other companies simply cannot compare with.</span> Our team of experts consistently goes above and beyond, ensuring that clients not only <span class="hl">get the support they need but also receive the strategic guidance necessary to stay ahead in an ever-evolving digital landscape.</span></p>
    <p style="margin-top:13.4px">Our <span class="hl">90-day performance review</span> process ensures that we continuously improve our service based on client feedback. This process allows us to <span class="hl">adapt, refine, and enhance our approach,</span> providing a truly personalized IT experience that aligns with business objectives.</p>
  </div>

  <div class="rule"></div>

  <h2 class="section-title" style="left:45px;top:503px"><span class="section-mark"></span>A Legacy of Trust &amp; Reliability</h2>
  <div class="abs body-copy" style="left:45px;top:536px;width:440px;line-height:13.4px">
    <p>The fact that many of our clients have remained with us for <span class="hl">decades without a formal contract</span> speaks volumes about the trust we have built. We don’t lock in clients with paperwork—we keep them with results. <span class="hl">That’s the difference between a standard managed IT provider and an IT partner who genuinely cares.</span></p>
  </div>

  <div class="closing">If you’re looking for an IT provider that will treat your business as if it were their own, look no further. Our legacy of service, innovation, and commitment to our clients is what sets us apart from the rest.</div>
</section>

</body>
</html>
```